trading data display webpage

We have build a rough wireframe of the two webpages that we want to display .The two wireframes are attached as a pdf document.
there will be login page. after login , the user will see the index page. that is the first page of the wireframe.

what we are displaying is essentially spread data. we are taking the difference in prices are two places and displaying the data. some calculations are done and is shown in the grid.

below the grid we show the behaviour on a graph. we will use bubble chart. I did not find a sample, hence have thrown in a placeholder.

this is time series data ( changes daily) and hence we need to check the behaviour.

the second wire frame shows how the user will choose the source price points and the destination price points.
we are talking here of natural gas prices hence the reference to source prices and destination prices.

you need to design the page/ pages such that the end-user loves it and is easy to use. the intent here is easy to use and easy to understand.
this will be responsive webpage since the end user will check it out on a tablet or a smartphone.

so if possible tell us how the navigation bar, the button bar, etc should fall when the screen size decreases.

I have uploaded 2 files. one is the wireframe ( pdf document) and second is the logo file.

please also let us know where to place the logo.

Target Market(s)

the target market is traders and data analyst

Industry/Entity Type

Build

Colors

Designer to choose colors to be used in the design.

Requirements
Must have
• 1. design for the web.
2. but think how the design will look when the screen size decreases.
3. tell if possible what screen components to keep and what to hide.

```html
<!DOCTYPE html>
<html lang="en">
<head>
<meta charset="utf-8">
<title>Gasline – Spread Dashboard</title>
<link href="https://fonts.googleapis.com/css2?family=Open+Sans:wght@300;400;600&display=swap" rel="stylesheet">
<style>
:root{
  --page:#f6f6f6;
  --white:#ffffff;
  --line:#e2e2e2;
  --text:#555555;
  --text-dark:#444444;
  --muted:#888888;
  --green:#8cc43f;
  --blue:#0155a5;
  --orange-dark:#f46a25;
  --orange-mid:#ff8445;
  --orange-light:#ffa072;
  --chart-blue:#a9d0da;
  --chart-orange:#f4866a;
}
*{box-sizing:border-box;margin:0;padding:0}
html,body{width:1200px;height:1110px;overflow:hidden}
body{background:var(--page);font-family:"Open Sans",sans-serif;color:var(--text);position:relative}

.site-header{position:absolute;left:0;top:0;width:1200px;height:101px;background:var(--white);border-bottom:1px solid var(--line)}
.brand{position:absolute;left:124px;top:34px;display:flex;align-items:center;gap:10px;font-size:26px;font-weight:600;color:var(--blue)}
.brand-dot{width:30px;height:30px;border-radius:50%;background:var(--green)}
.main-nav{position:absolute;left:331px;top:36px;display:flex;align-items:center;gap:18px}
.nav-home{background:var(--green);color:var(--white);font-weight:600;font-size:15px;padding:6px 14px;border-radius:3px}
.nav-link{color:var(--muted);font-size:16px}
.user{position:absolute;left:840px;top:29px;display:flex;align-items:center;gap:11px}
.avatar{width:48px;height:48px;border-radius:50%;background:linear-gradient(135deg,#6b6f78,#c9ccd2)}
.user-name{font-size:19px;color:var(--text-dark);line-height:22px}
.user-mail{font-size:14px;color:var(--muted)}

.region-tabs{position:absolute;left:128px;top:169px;display:flex;gap:9px;align-items:flex-end}
.tab{height:42px;padding:0 22px;font-size:17px;display:flex;align-items:center;color:var(--white);background:var(--blue);border-radius:2px 2px 0 0}
.tab.active{background:var(--white);color:var(--text-dark);height:45px;border:1px solid var(--line);border-bottom:none;position:relative;z-index:2}

.panel{position:absolute;left:128px;top:212px;width:928px;height:817px;background:var(--white);border:1px solid var(--line);border-radius:2px;box-shadow:0 1px 2px rgba(0,0,0,.08)}
.filters{height:98px;position:relative;border-bottom:1px solid var(--line)}
.select{position:absolute;top:23px;height:50px;border:1px solid #d8d8d8;border-radius:3px;display:flex;align-items:center;font-size:18px;color:var(--text)}
.select span{padding-left:18px;flex:1}
.select i{width:46px;height:100%;border-left:1px solid #d8d8d8;display:flex;align-items:center;justify-content:center}
.select.source{left:25px;width:216px}
.select.dest{left:660px;width:242px}

.toolbar{height:87px;background:var(--page);position:relative}
.btn-group{position:absolute;top:23px;display:flex;border:1px solid #d2d2d2;border-radius:3px;overflow:hidden;background:#f0f0f0}
.btn-group span{padding:0 16px;height:40px;display:flex;align-items:center;gap:6px;font-size:16px;border-right:1px solid #d2d2d2;color:var(--text-dark)}
.btn-group span:last-child{border-right:none}
.btn-group .on{background:linear-gradient(#c4c4c4,#b4b4b4);color:#555}
.range{left:23px}
.period{right:23px;background:var(--white)}
.period span{height:38px}

.data-table{width:100%;border-collapse:collapse;font-size:15px}
.data-table th{height:43px;font-weight:600;font-size:16px;color:var(--text-dark);background:linear-gradient(#f0f0f0,#e4e4e4);border-right:1px solid #d9d9d9;border-bottom:1px solid #d4d4d4}
.data-table td{color:var(--muted);border-right:1px solid var(--line);border-bottom:1px solid var(--line);padding-left:25px}
.data-table th:last-child,.data-table td:last-child{border-right:none}
.data-table tr:nth-child(1) td{height:51px}
.data-table tr:nth-child(2) td{height:51px}
.data-table tr:nth-child(3) td{height:48px}
.data-table tr:nth-child(4) td{height:47px}

.chart-title{position:absolute;font-size:21px;font-weight:300;color:var(--text);top:505px}
.pie-title{left:93px}
.line-title{left:447px}
.divider{position:absolute;left:383px;top:517px;width:1px;height:229px;background:var(--line)}
.pie{position:absolute;left:84px;top:557px}
.pie-label{position:absolute;font-size:14px;color:var(--text-dark)}
.line-chart{position:absolute;left:442px;top:558px}

.footer{position:absolute;top:1063px;left:0;width:1200px;text-align:center;font-size:14px;color:var(--text)}
</style>
</head>
<body>
<header class="site-header">
  <div class="brand"><span class="brand-dot"></span>Gasline</div>
  <nav class="main-nav"><span class="nav-home">Home</span><span class="nav-link">Profile page</span></nav>
  <div class="user">
    <div class="avatar" role="img" aria-label="User profile photo"></div>
    <div><div class="user-name">Rohan Varma</div><div class="user-mail">rohan@example.net</div></div>
  </div>
</header>

<div class="region-tabs">
  <span class="tab active">EAST</span>
  <span class="tab">CENTRAL</span>
  <span class="tab">WEST</span>
</div>

<main class="panel">
  <div class="filters">
    <div class="select source"><span>Source Indices</span><i><svg width="12" height="8" viewBox="0 0 12 8"><path d="M2 2l4 4 4-4" fill="none" stroke="#666" stroke-width="1.5"/></svg></i></div>
    <div class="select dest"><span>Destination Indices</span><i><svg width="12" height="8" viewBox="0 0 12 8"><path d="M2 2l4 4 4-4" fill="none" stroke="#666" stroke-width="1.5"/></svg></i></div>
  </div>
  <div class="toolbar">
    <div class="btn-group range"><span>5 Days</span><span>7 Days</span><span class="on">18 Days</span></div>
    <div class="btn-group period">
      <span><svg width="15" height="15" viewBox="0 0 15 15"><rect x="1" y="2.5" width="13" height="11" fill="none" stroke="#555" stroke-width="1.4"/><path d="M1 6h13M4 1v3M11 1v3M5 6v7.5M8 6v7.5M11 6v7.5M1 9.5h13" stroke="#555" stroke-width="1.1"/></svg>Month</span>
      <span><svg width="15" height="15" viewBox="0 0 15 15"><rect x="1" y="2.5" width="13" height="11" fill="none" stroke="#555" stroke-width="1.4"/><path d="M1 6h13M4 1v3M11 1v3M5 6v7.5M8 6v7.5M11 6v7.5M1 9.5h13" stroke="#555" stroke-width="1.1"/></svg>Year</span>
    </div>
  </div>

  <table class="data-table">
    <colgroup><col style="width:142px"><col style="width:133px"><col style="width:115px"><col style="width:110px"><col style="width:127px"><col style="width:129px"><col></colgroup>
    <thead><tr><th>Spread Name</th><th>Avg Spread</th><th>+ ve Prob</th><th>- ve Prob</th><th>Spike prob</th><th>Avg Supply</th><th>Supply cut prob</th></tr></thead>
    <tbody>
      <tr><td>Spread 1</td><td>Items #1</td><td>150</td><td>150</td><td>567 %</td><td>567 %</td><td>567 %</td></tr>
      <tr><td>Spread 1</td><td>Items #1</td><td>150</td><td>150</td><td>567 %</td><td>567 %</td><td>567 %</td></tr>
      <tr><td>Spread 1</td><td>Items #1</td><td>150</td><td>150</td><td>567 %</td><td>567 %</td><td>567 %</td></tr>
      <tr><td>Spread 1</td><td>Items #1</td><td>150</td><td>150</td><td>567 %</td><td>567 %</td><td>567 %</td></tr>
    </tbody>
  </table>

  <h2 class="chart-title pie-title">Spread v/s supply</h2>
  <h2 class="chart-title line-title">Spreads across time</h2>
  <div class="divider"></div>

  <svg class="pie" width="190" height="190" viewBox="-95 -95 190 190">
    <circle r="92" fill="var(--orange-dark)"/>
    <path d="M0 0L0 -92A92 92 0 0 1 75.4 -52.8Z" fill="var(--orange-light)"/>
    <path d="M0 0L75.4 -52.8A92 92 0 0 1 52.8 75.4Z" fill="var(--orange-mid)"/>
  </svg>
  <span class="pie-label" style="left:242px;top:552px">20%</span>
  <span class="pie-label" style="left:288px;top:655px">30%</span>

  <svg class="line-chart" width="430" height="180" viewBox="608 821 458.7 192" font-family="Arial, sans-serif">
    <g stroke="#e6e6e6" stroke-dasharray="3 3">
      <line x1="651" y1="835" x2="1046" y2="835"/><line x1="651" y1="885" x2="1046" y2="885"/><line x1="651" y1="935" x2="1046" y2="935"/>
    </g>
    <g stroke="#eeeeee"><line x1="752" y1="835" x2="752" y2="985"/><line x1="852" y1="835" x2="852" y2="985"/><line x1="952" y1="835" x2="952" y2="985"/><line x1="1046" y1="835" x2="1046" y2="985"/></g>
    <line x1="651" y1="985" x2="1046" y2="985" stroke="#cccccc"/>
    <path d="M652 914L702 895L752 856L802 878L852 865L902 903L952 914L1003 884L1046 842L1046 985L652 985Z" fill="#eef5f8" opacity=".7"/>
    <path d="M652 941L702 948L752 941L802 948L852 960L902 959L952 947L1003 956L1046 965L1046 985L652 985Z" fill="#fdf2ec"/>
    <polyline points="652,914 702,895 752,856 802,878 852,865 902,903 952,914 1003,884 1046,842" fill="none" stroke="var(--chart-blue)" stroke-width="2"/>
    <polyline points="652,941 702,948 752,941 802,948 852,960 902,959 952,947 1003,956 1046,965" fill="none" stroke="var(--chart-orange)" stroke-width="2"/>
    <g fill="#fff" stroke="var(--chart-blue)" stroke-width="1.6">
      <circle cx="652" cy="914" r="3.2"/><circle cx="702" cy="895" r="3.2"/><circle cx="752" cy="856" r="3.2"/><circle cx="802" cy="878" r="3.2"/><circle cx="852" cy="865" r="3.2"/><circle cx="902" cy="903" r="3.2"/><circle cx="952" cy="914" r="3.2"/><circle cx="1003" cy="884" r="3.2"/>
    </g>
    <g fill="#fff" stroke="var(--chart-orange)" stroke-width="1.6">
      <circle cx="652" cy="941" r="3.2"/><circle cx="702" cy="948" r="3.2"/><circle cx="752" cy="941" r="3.2"/><circle cx="802" cy="948" r="3.2"/><circle cx="852" cy="960" r="3.2"/><circle cx="902" cy="959" r="3.2"/><circle cx="952" cy="947" r="3.2"/><circle cx="1003" cy="956" r="3.2"/>
    </g>
    <rect x="886" y="870" width="32" height="19" rx="3" fill="#3a3a3a"/>
    <path d="M897 889L902 894L907 889Z" fill="#3a3a3a"/>
    <text x="902" y="883.5" font-size="10" fill="#fff" text-anchor="middle">823</text>
    <g font-size="10" fill="#777" text-anchor="end">
      <text x="642" y="839">1,500</text><text x="642" y="889">1,000</text><text x="642" y="939">500</text>
    </g>
    <g font-size="10" fill="#777" text-anchor="middle">
      <text x="668" y="1003">27 May</text><text x="768" y="1003">29 May</text><text x="868" y="1004">31 May</text><text x="966" y="1004">02 Jun</text>
    </g>
  </svg>
</main>

<footer class="footer">© Copyright 2013 Gasline, All Rights Reserved.</footer>
</body>
</html>
```